'Ormel Property Development' Business Card

Business Card Features:

High Quality (potentially textured) thick card - preference is white textured card

Logo (supplied)

We plan to use the vertical logo as the main logo. But i am happy for people to use either if they find it works better for the design of the card.

The building icon and also the insert to the 'E' is in a metallic finish, i think this should be finished in a metallic embossed or raised style.
Updates

Please note i have attached both a horizontal and Vertical Logo for your reference. We plan to use the vertical logo as the main logo. But i am happy for people to use either if they find it works better for the design of the card.

Please note i am considering having the cards made on stainless steel. This introduces the option of having cut outs in the card and etching or printing for the design. If you have a good concept for this please submit.

http://www.tinquarry.example/black-metal-cards# this is a site that makes the metal cards to offer some direction . . . . Please note i am basic the selection o the best design, if that means normal print cards on paper then this is what i will choose. But there are some great options with the metal. Thanks.

Industry/Entity Type

Building

Requirements
Must have
• Helvetica font to details side of card - logo as supplied to opposite side.

Card Details:

Darrow Pketts
Managing Director

+61 487 263 518
+61 3 6172 4809

PO Box 73
Bentleigh, VIC 3024

darrow@ormel.example

www.ormel.example

```html
<!DOCTYPE html>
<html lang="en">
<head>
<meta charset="utf-8">
<title>Ormel Property Development – Business Card</title>
<link rel="stylesheet" href="https://fonts.googleapis.com/css2?family=Arimo:wght@400;700&family=Questrial&display=swap">
<style>
  :root {
    --backdrop: #2b2b2d;
    --orange: #f7941d;
    --band-grey: #a9aaad;
    --charcoal: #535959;
    --metal: #9c9d9f;
    --white: #ffffff;
    --paper: #eceeee;
  }
  * { box-sizing: border-box; margin: 0; padding: 0; }
  html, body {
    width: 1200px; height: 800px; overflow: hidden;
    background: var(--backdrop);
  }
  .canvas { position: relative; width: 1200px; height: 800px; }

  .card {
    position: absolute; top: 257px;
    width: 500px; height: 286px;
    overflow: hidden;
  }

  /* Front: details side */
  .card--front { left: 70px; background: var(--orange); }
  .title-band {
    position: absolute; left: 0; top: 42px;
    width: 100%; height: 94px;
    background: var(--band-grey);
  }
  .person { position: absolute; left: 28px; top: 10px; }
  .person__name {
    font-family: "Questrial", sans-serif;
    font-size: 18px; color: var(--white);
  }
  .person__role {
    font-family: "Arimo", sans-serif;
    font-size: 9px; color: var(--charcoal);
    margin-top: 1px;
  }
  .division {
    position: absolute; right: 22px; bottom: 12px;
    font-family: "Arimo", sans-serif; font-weight: 700;
    font-size: 22px; letter-spacing: 1.5px;
    font-variant: small-caps; color: var(--white);
  }

  .contacts {
    position: absolute; left: 22px; top: 152px;
    list-style: none;
  }
  .contacts li {
    display: flex; align-items: center; gap: 10px;
    height: 21px;
    font-family: "Arimo", sans-serif; font-size: 11px;
    color: var(--white);
  }
  .contacts svg { width: 12px; height: 12px; fill: var(--charcoal); flex: none; }

  .wordmark {
    position: absolute; right: 26px; bottom: 22px;
    display: flex; align-items: center; gap: 10px;
  }
  .wordmark__name {
    font-family: "Questrial", sans-serif;
    font-size: 66px; line-height: 1; color: var(--charcoal);
  }
  .wordmark__mark { width: 16px; height: 16px; background: var(--metal); }

  /* Back: logo side */
  .card--back {
    left: 630px; background: var(--paper);
    display: flex; align-items: center; justify-content: center;
  }
  .card--back .wordmark { position: static; }
  .card--back .wordmark__name { font-size: 80px; }
</style>
</head>
<body>
<main class="canvas">

  <section class="card card--front" aria-label="Business card, details side">
    <div class="title-band">
      <div class="person">
        <p class="person__name">Darrow Pketts</p>
        <p class="person__role">Managing Director</p>
      </div>
      <p class="division">Property Development</p>
    </div>

    <ul class="contacts">
      <li>
        <svg viewBox="0 0 12 12" aria-hidden="true"><path d="M3 0h6a1 1 0 0 1 1 1v10a1 1 0 0 1-1 1H3a1 1 0 0 1-1-1V1a1 1 0 0 1 1-1zm0 1.5v7.5h6V1.5z"/></svg>
        0487 263 518
      </li>
      <li>
        <svg viewBox="0 0 12 12" aria-hidden="true"><path d="M2.4 0.5l2 2.3-1 1.4c.7 1.6 2 2.9 3.5 3.6l1.4-1 2.2 2-1.3 2.1C5 10.7 1.3 7 .3 1.8z"/></svg>
        1800 604 117
      </li>
      <li>
        <svg viewBox="0 0 12 12" aria-hidden="true"><path d="M6 0a6 6 0 1 0 0 12A6 6 0 0 0 6 0zm0 3a3 3 0 1 1 0 6 3 3 0 0 1 0-6z"/></svg>
        darrow@ormel.example
      </li>
      <li>
        <svg viewBox="0 0 12 12" aria-hidden="true"><path d="M6 0a4 4 0 0 0-4 4c0 3 4 8 4 8s4-5 4-8a4 4 0 0 0-4-4zm0 2.5a1.5 1.5 0 1 1 0 3 1.5 1.5 0 0 1 0-3z"/></svg>
        www.ormel.example
      </li>
      <li>
        <svg viewBox="0 0 12 12" aria-hidden="true"><path d="M0 2h12v8H0zm1 1l5 3.5L11 3z"/></svg>
        PO BOX 73 BENTLEIGH VIC 3024
      </li>
    </ul>

    <div class="wordmark">
      <span class="wordmark__name">Ormel</span>
      <span class="wordmark__mark" aria-hidden="true"></span>
    </div>
  </section>

  <section class="card card--back" aria-label="Business card, logo side">
    <div class="wordmark">
      <span class="wordmark__name">Ormel</span>
      <span class="wordmark__mark" aria-hidden="true"></span>
    </div>
  </section>

</main>
</body>
</html>
```